DeedVault Site Introduction and overview Flyer

We need a flyer made that gives an over view of our business. We are a land and mineral records company based in Texas that provides data to many different industries. This should be a bi-fold flyer that measures a 6" x 6" square. The designs should incorporate our company colors with subtle uses of the brighter colors from our new website. Logo and new website pictures are uploaded below.
we would like for the inside left to contain a brief company description: " Since 2005, DeedVault has provided online access to courthouse records and mineral ownership data. Our data, search and order management tools allow you to quickly build and store chains of title, division orders and contact lists. No other website provides as comprehensive of a data set. Start searching DeedVault today.
The front should contain a relevant photo, logo and website name.
the back should contain our contact information and graphic.
the inside right should contain 5 major bullet points with appropriate icons. the bullet points will be:
1. County Courthouse Records Available in Texas, Colorado, New Mexico, and Oklahoma
2. Search all Texas counties at once with Broadscan Lookup
3. Search mineral ownership data from across the State of Texas
4. Download bulk mineral appraisal rolls
5. Plats available in select counties

Target Market(s)
Oil & Gas, Legal, Surveyors, Title, Real Estate, male and female
Industry/Entity Type
Business
Font styles to use
Colors
Designer to choose colors to be used in the design.
Requirements
Must have
- Simplicity.
- relevant colors/graphics

Nice to have
- we would like to have the graphic shown in the sitecapture 2 used, if possible

Should not have
- non-relevant colors, graphics

```html
<!DOCTYPE html>
<html lang="en">
<head>
<meta charset="utf-8">
<title>DeedVault Bi-fold Flyer</title>
<link href="https://fonts.googleapis.com/css2?family=Work+Sans:wght@400;500;700&display=swap" rel="stylesheet">
<style>
  :root{
    --canvas:#d1d2d4;
    --paper:#f8f8f9;
    --white:#ffffff;
    --navy:#1f2f93;
    --slate:#7784ad;
    --ink:#3b3f4c;
    --photo-dark:#2a3454;
    --photo-mid:#6d7796;
    --sky-top:#6f7eb1;
    --sky-low:#3b4a86;
    --accent:#38a8d8;
  }
  *{margin:0;padding:0;box-sizing:border-box}
  html,body{width:1162px;height:1200px;overflow:hidden}
  body{background:var(--canvas);font-family:"Work Sans",sans-serif;color:var(--ink);position:relative}
  .spread{position:absolute;left:178px;width:807px}
  .spread-outer{top:179px;height:403px}
  .spread-inner{top:624px;height:404px;background:var(--white)}
  .page{position:absolute;top:0;height:100%;width:404px;overflow:hidden}
  .page-left{left:0}
  .page-right{left:403px}

  /* front cover */
  .cover{background:var(--paper)}
  .cover .brand{position:absolute;left:36px;top:38px}
  .cover-photo{position:absolute;left:0;top:108px;width:100%;height:295px;
    background:linear-gradient(180deg,#8c95b1 0%,#7680a0 45%,#4a5474 80%,var(--photo-dark) 100%)}
  .url-tag{position:absolute;background:var(--slate);color:var(--white);font-size:11px;letter-spacing:1.2px;
    display:flex;align-items:center;justify-content:center}
  .cover .url-tag{left:252px;top:368px;width:152px;height:18px}

  /* back cover */
  .back{background:var(--paper)}
  .back-photo{position:absolute;left:0;top:0;width:100%;height:171px;
    background:linear-gradient(180deg,#5c6686 0%,#7b84a0 45%,#4a5474 62%,#2c3656 100%)}
  .back .brand{position:absolute;left:0;right:0;top:284px;text-align:center;justify-content:center}
  .address{position:absolute;left:0;right:0;top:340px;text-align:center;font-size:9.5px;line-height:12px;color:#222}
  .contacts{position:absolute;left:0;right:0;top:373px;display:flex;justify-content:center;gap:10px;font-size:9.5px;color:#222}
  .contacts span{display:flex;align-items:center;gap:3px}

  .brand{display:flex;align-items:center;gap:6px;font-weight:700;color:var(--navy);letter-spacing:-.3px}
  .brand .mark{display:block;background:var(--navy)}
  .cover .brand{font-size:20px}
  .cover .brand .mark{width:10px;height:10px}
  .back .brand{font-size:26px}
  .back .brand .mark{width:12px;height:12px}

  /* inside */
  .inside-photo{position:absolute;left:0;top:0;width:807px;height:237px;
    background:linear-gradient(180deg,var(--sky-top) 0%,#5665a0 40%,var(--sky-low) 62%,#2f3d6f 100%)}
  .fold-shade{position:absolute;left:396px;top:0;width:22px;height:404px;
    background:linear-gradient(90deg,rgba(255,255,255,0) 0%,rgba(255,255,255,.18) 45%,rgba(0,0,0,.06) 60%,rgba(255,255,255,0) 100%)}
  .tagline{position:absolute;left:59px;top:99px;width:290px;padding-left:12px;border-left:1px solid rgba(255,255,255,.8);
    color:var(--white);font-size:10.2px;line-height:12.5px;text-align:justify}
  .inside .brand-light{position:absolute;left:515px;top:80px;color:var(--white);font-weight:700;font-size:22px;display:flex;align-items:center;gap:6px}
  .brand-light .mark{width:11px;height:11px;background:var(--white);display:block}

  .side-bar{position:absolute;left:0;top:237px;width:27px;height:167px;background:var(--slate)}
  .side-bar::after{content:"";position:absolute;left:27px;top:74px;border-top:11px solid transparent;border-bottom:11px solid transparent;border-left:11px solid var(--slate)}
  .intro{position:absolute;left:77px;top:271px;width:276px;font-size:11.4px;line-height:13.2px;text-align:justify;color:#4a4e5c}

  .features{position:absolute;list-style:none}
  .features li{display:flex;align-items:flex-start;gap:7px;font-size:9.3px;line-height:11px;color:#4f5668;margin-bottom:10px}
  .features .icon{flex:none;width:20px;height:20px;border-radius:50%;background:var(--slate);display:flex;align-items:center;justify-content:center}
  .features .icon svg{width:12px;height:12px}
  .features-a{left:444px;top:271px;width:170px}
  .features-b{left:630px;top:271px;width:150px}
  .inside .url-tag{left:640px;top:381px;width:167px;height:23px;font-size:11.5px;letter-spacing:.4px}
</style>
</head>
<body>

<section class="spread spread-outer">
  <article class="page page-left cover">
    <div class="brand"><span class="mark"></span>DeedVault</div>
    <div class="cover-photo" role="img" aria-label="Photo of oil pumpjacks silhouetted against a hazy sky"></div>
    <div class="url-tag">www.deedvault.com</div>
  </article>
  <article class="page page-right back">
    <div class="back-photo" role="img" aria-label="Photo of an offshore oil platform at sea under a cloudy sky"></div>
    <div class="brand"><span class="mark"></span>DeedVault</div>
    <p class="address">4410 Cedar Ridge Dr, Suite 120<br>Round Rock, TX 78681</p>
    <div class="contacts">
      <span><svg width="9" height="9" viewBox="0 0 12 12" fill="none" stroke="var(--accent)" stroke-width="1.3"><path d="M3 1l2 2.5-1.2 1.4a7 7 0 0 0 3.3 3.3L8.5 7 11 9l-1 2C5 11 1 7 1 2z"/></svg>(512) 555-0184</span>
      <span><svg width="9" height="9" viewBox="0 0 12 12" fill="none" stroke="var(--accent)" stroke-width="1.3"><rect x="1" y="2.5" width="10" height="7"/><path d="M1 2.5l5 4 5-4"/></svg>hello@deedvault.com</span>
      <span><svg width="9" height="9" viewBox="0 0 12 12" fill="none" stroke="var(--accent)" stroke-width="1.1"><circle cx="6" cy="6" r="5"/><path d="M1 6h10M6 1c-2.5 3-2.5 7 0 10M6 1c2.5 3 2.5 7 0 10"/></svg>www.deedvault.com</span>
    </div>
  </article>
</section>

<section class="spread spread-inner inside">
  <div class="inside-photo" role="img" aria-label="Photo of a river canyon landscape with cliffs at dusk"></div>
  <p class="tagline">DeedVault is the premier source for County Clerk Records and Mineral Appraisal Data covering Texas, Oklahoma, New Mexico and Colorado.</p>
  <div class="brand-light"><span class="mark"></span>DeedVault</div>
  <div class="fold-shade"></div>

  <div class="side-bar"></div>
  <p class="intro">Since 2005, DeedVault has provided online access to courthouse records and mineral ownership data. Our data, search and order management tools allow you to quickly build and store chains of title, division orders and contact lists. No other website provides as comprehensive of a data set. Start searching DeedVault today.</p>

  <ul class="features features-a">
    <li><span class="icon"><svg viewBox="0 0 12 12" fill="none" stroke="#fff" stroke-width="1"><path d="M1 4l5-3 5 3zM2 5v5M4.5 5v5M7.5 5v5M10 5v5M1 11h10"/></svg></span>County Courthouse Records Available in Texas, Colorado, New Mexico, and Oklahoma</li>
    <li><span class="icon"><svg viewBox="0 0 12 12" fill="none" stroke="#fff" stroke-width="1.1"><rect x="2" y="1" width="8" height="10"/><circle cx="6" cy="5.5" r="2"/><path d="M7.4 7l1.6 1.8"/></svg></span>Search all Texas counties at once with Broadscan Lookup</li>
    <li><span class="icon"><svg viewBox="0 0 12 12" fill="none" stroke="#fff" stroke-width="1.1"><path d="M1 11l4-4M5 7l4-5 2 2-5 4zM2 6l3 2"/></svg></span>Search mineral ownership data from across the State of Texas</li>
  </ul>
  <ul class="features features-b">
    <li><span class="icon"><svg viewBox="0 0 12 12" fill="none" stroke="#fff" stroke-width="1.1"><path d="M6 1v7M3 5l3 3 3-3M1 8v3h10V8"/></svg></span>Download bulk mineral appraisal rolls</li>
    <li><span class="icon"><svg viewBox="0 0 12 12" fill="#fff"><circle cx="3.5" cy="3.5" r="1.8"/><circle cx="8.5" cy="3.5" r="1.8"/><circle cx="3.5" cy="8.5" r="1.8"/><circle cx="8.5" cy="8.5" r="1.8"/></svg></span>Plats available in select counties</li>
  </ul>
  <div class="url-tag">www.deedvault.com</div>
</section>

</body>
</html>
```